Internal Designs and HTML Prototype

A Home page design has been completed. The remaining 6 pages need to be designed based on the provided wireframes and the home page design. HTML conversion to be performed to the following standards; - XHTML 1.0 Transitional - Fixed width - Cross-browser compatibility - Safari 2&3, Opera 9 etc - Relative Font sizes - Table-less forms - JQuery as preferred Javascript library - SEO and loading optimoisation

The selected designer will be required to provide the HTML prototype for their layouts.

Target Market(s)

Ensure style of provided Home page is followed.

Industry/Entity Type

Real Estate

```html
<!DOCTYPE html>
<html lang="en">
<head>
<meta charset="utf-8">
<title>Homeswitch – My Property View</title>
<link rel="stylesheet" href="https://fonts.googleapis.com/css2?family=Arimo:wght@400;700&family=Dancing+Script:wght@500&display=swap">
<style>
:root{
  --orange:#f26a1b;
  --orange-dark:#e0470f;
  --red-band:#e8401c;
  --green-dark:#2e7d1f;
  --green-bar:#3f8f25;
  --green-text:#7ab829;
  --green-label:#2f6d14;
  --row-head:#d3e3a9;
  --row-light:#eaf2d6;
  --row-mid:#e1ecc3;
  --page-bg:#dcebcc;
  --frame:#6d8a74;
  --tab:#6f8a78;
  --link-red:#e2371b;
  --peach:#fcd9bd;
  --white:#ffffff;
  --grey:#9aa39a;
}
*{box-sizing:border-box;margin:0;padding:0}
html,body{width:1200px;height:1184px;overflow:hidden}
body{position:relative;background:var(--page-bg);font-family:"Arimo",Arial,sans-serif;color:var(--green-text)}
.abs{position:absolute}

/* header */
.header-photo{left:0;top:0;width:1200px;height:210px;background:linear-gradient(90deg,#3f7a1c 0%,#5c9a2c 45%,#6fa83a 70%,#8bbf55 100%)}
.brand{left:34px;top:38px;width:282px;height:140px;display:flex;align-items:center;gap:14px;padding-left:22px}
.brand-square{width:46px;height:46px;background:var(--orange);border-radius:8px}
.brand-name{font-size:42px;font-weight:700;color:var(--white)}
.tag-band{left:0;top:210px;width:1200px;height:52px;background:linear-gradient(180deg,#f05a2a,var(--red-band))}
.tagline{left:34px;top:220px;font-size:29px;color:var(--white)}
.login{left:684px;top:228px;display:flex;align-items:center;gap:6px;font-size:11px;font-weight:700;color:var(--white);letter-spacing:.5px}
.login input{width:130px;height:17px;border:none;background:var(--white)}
.login .gap{width:8px}
.login button{height:17px;padding:0 10px;border:1px solid #ddd;background:#c7cfc8;color:var(--white);font:700 10px "Arimo",Arial,sans-serif;letter-spacing:1px}

/* frame */
.frame{left:162px;top:285px;width:1022px;height:840px;border-radius:22px;background:var(--frame)}
.panel{left:171px;top:297px;width:998px;height:805px;border-radius:16px;background:linear-gradient(90deg,var(--white) 35%,#fff4ea 70%,var(--peach) 100%)}

/* nav */
.nav-tab{left:18px;width:147px;height:82px;border-radius:12px 0 0 12px;background:var(--tab);border:4px solid #c6d3c4;border-right:none;display:flex;align-items:center;justify-content:center;text-align:center;color:var(--white);font-weight:700;font-size:20px;line-height:1.3}
.nav-tab.active{background:var(--white);color:var(--orange-dark);width:160px;border-color:#c6d3c4}

/* content */
.title-my{left:200px;top:308px;font-family:"Dancing Script",cursive;font-size:40px;color:#8a8f88}
.title-main{left:203px;top:352px;font-size:31px;font-weight:700;color:var(--orange)}
.add-listing{left:1019px;top:337px;width:121px;height:43px;border-radius:14px;background:var(--orange);color:var(--white);font-size:16px;display:flex;align-items:center;justify-content:center}
.account-links{right:64px;top:403px;font-size:13px;color:var(--link-red)}
.account-links span{margin:0 4px;color:#999}
.listing-bar{left:207px;top:439px;width:936px;height:30px;border-radius:0 12px 12px 0;background:linear-gradient(180deg,#4ea22c,var(--green-dark));color:var(--white);font-size:16px;padding:6px 16px;display:flex;justify-content:space-between}
.bar-icons{display:flex;gap:16px;align-items:center;font-size:14px}
.bar-icons svg{vertical-align:middle;margin-right:4px}
.listed-by{left:203px;top:483px;font-size:15px}
.listed-by a{color:var(--link-red);text-decoration:none}
.photo{left:205px;top:523px;width:300px;height:211px;background:linear-gradient(180deg,#0d1f55 0%,#1d3a7a 55%,#6b5a3c 85%,#3d4a2a 100%)}
.more-photos{left:348px;top:744px;display:flex;align-items:center;gap:10px;font-size:15px;color:var(--link-red)}
.more-photos .dot{width:26px;height:26px;border-radius:50%;background:var(--orange-dark)}
.map{left:205px;top:794px;width:300px;height:211px;background:linear-gradient(135deg,#e9e6dd,#f1eee4 50%,#e3e0d4)}

.details{left:509px;top:523px;width:634px}
.row{height:24px;padding-left:14px;font-size:14px;display:flex;align-items:center;background:var(--row-light)}
.row:nth-child(even){background:var(--row-mid)}
.row.head{background:var(--row-head);color:var(--green-label)}
.row .label{width:175px}
.side-links{left:959px;top:800px;font-size:12px;line-height:17px;color:var(--link-red)}
.printer{left:1020px;top:1145px;font-size:11px;letter-spacing:.5px;color:var(--grey)}
</style>
</head>
<body>

<header>
  <div class="abs header-photo" role="img" aria-label="Photo of a family lying on green grass"></div>
  <div class="abs brand"><span class="brand-square"></span><span class="brand-name">Homeswitch</span></div>
  <div class="abs tag-band"></div>
  <p class="abs tagline">The place to sell. The place to buy.</p>
  <form class="abs login">
    <label>USER NAME</label><input type="text">
    <span class="gap"></span>
    <label>PASSWORD</label><input type="password">
    <button type="button">SIGN IN</button>
  </form>
</header>

<div class="abs frame"></div>
<main class="abs panel"></main>

<nav>
  <a class="abs nav-tab" style="top:289px">Home</a>
  <a class="abs nav-tab" style="top:384px">Property<br>Search</a>
  <a class="abs nav-tab" style="top:478px">How<br>It Works</a>
  <a class="abs nav-tab active" style="top:571px">My<br>Account</a>
  <a class="abs nav-tab" style="top:662px">Contact</a>
</nav>

<h1>
  <span class="abs title-my">My</span>
  <span class="abs title-main">PROPERTY VIEW</span>
</h1>
<a class="abs add-listing">ADD LISTING</a>
<p class="abs account-links">REGISTRATION DETAILS<span>|</span>MY PROPERTIES<span>|</span>MY MESSAGES<span>|</span>MY SHORTLIST<span>|</span>EDIT REGISTRATION DETAILS</p>

<div class="abs listing-bar">
  <span>WILLOWBRAE</span>
  <span class="bar-icons">
    <span><svg width="26" height="12" viewBox="0 0 26 12"><rect x="1" y="4" width="24" height="6" fill="#f5a623"/><rect x="1" y="1" width="4" height="9" fill="#f5a623"/></svg>4</span>
    <span><svg width="14" height="22" viewBox="0 0 14 22"><path d="M3 21V4a3 3 0 0 1 6 0" stroke="#fff" stroke-width="2" fill="none"/><path d="M8 6l4 8" stroke="#fff" stroke-width="1.5"/></svg>4</span>
    <span><svg width="26" height="14" viewBox="0 0 26 14"><path d="M2 9l3-6h14l4 6v3H2z" fill="#f5a623"/><circle cx="7" cy="12" r="2" fill="#fff"/><circle cx="19" cy="12" r="2" fill="#fff"/></svg>3</span>
  </span>
</div>

<p class="abs listed-by">Listed by ph4 <a>(Enquire)</a></p>
<div class="abs photo" role="img" aria-label="Photo of a two-storey house at dusk"></div>
<a class="abs more-photos"><span class="dot"></span>More photos (6)</a>
<div class="abs map" role="img" aria-label="Street map of the property location"></div>

<section class="abs details">
  <div class="row head">Location</div>
  <div class="row">Willowbrae 3912 VIC</div>
  <div class="row head">Asking Price</div>
  <div class="row">$500.000</div>
  <div class="row head">Property Features</div>
  <div class="row"><span class="label">Property type:</span><span>House</span></div>
  <div class="row"><span class="label">Bedrooms:</span><span>4</span></div>
  <div class="row"><span class="label">Bathrooms:</span><span>4</span></div>
  <div class="row"><span class="label">Carspaces:</span><span>3</span></div>
  <div class="row"><span class="label">Levels:</span><span>0</span></div>
  <div class="row"><span class="label">Year Built:</span><span>0</span></div>
  <div class="row"><span class="label">Counters:</span></div>
  <div class="row"><span class="label">Flooring:</span></div>
  <div class="row"><span class="label">Additional rooms:</span></div>
  <div class="row"><span class="label">Features:</span></div>
  <div class="row head">External Features:</div>
  <div class="row"><span class="label">Property size (sqm):</span><span>0</span></div>
  <div class="row"><span class="label">Land size (sqm):</span><span>0</span></div>
  <div class="row head">External Features:</div>
  <div class="row"></div>
  <div class="row head">Description:</div>
  <div class="row">Beach front property with amazing views</div>
</section>

<p class="abs side-links">Manage property searches<br>Manage property photos<br>Search for property match</p>

<p class="abs printer">PRINTER FRIENDLY VERSION</p>

</body>
</html>
```